Korvix App Graphics Design

Our application promotes location based self expression via pictures and text. The primary focus of the application is on the content posted and not on the person that posted it.

We want a very clean and fresh design that evokes positive energy. Our site is unique so our design should be as well. People will reveal thoughts on our site, so the design should convey a "revealing" feel. Our site is a place where people are comfortable to freely express themselves. Colors we have in mind are blue and green hues with earth tones for background.

Our project is to design ten screens for our Korvix application at resolution of 1136-by-640 pixels:

Feed Screen
Camera Screen
Post Screen
Check In Screen
Approval Screen
Map Screen
Flag Screen
Feed Select Screen
Export Screen
Menu Screen

In the contest phase we will require only three screens to be submitted. The screens we require to be submitted are: Feed Screen; Map Screen and Camera Screen. The designer we select as the winner of the competition will then complete the project and deliver a total of the ten screens described above in the handover phase.

We have attached a document below with detailed specs of each screen, we ask for your innovation to bring these screens to life through your design.
Updates

We want to clarify one aspect regarding the VISOR: the visor needs to be transparent so that when the picture scrolls underneath it, you can still see the picture underneath the visor.

Hi Everyone,

We have noticed that some designers need clarification regarding the visor element in the feed screen.
I have attached two examples to our brief area called:
Visor Example 1 and Visor Example 2

Please note that these are not the style we are looking for but are a good example to the concept of a Transparent Visor above the feed stream. We are looking for you guys to come up with a Visor concept that is consistent with the style of the design you are submitting.

Thanks,

Bo

Target Market(s)

People 17-40 who want to share their thought about the world around them.

Industry/Entity Type

Flag

Font styles to use
Sans Serif
Other font styles liked:
• We like “Helvetica New” or “Avenir” but are flexible

Requirements
Must have
• Visor component should look innovative.

```html
<!DOCTYPE html>
<html lang="en">
<head>
<meta charset="utf-8">
<title>Korvix App Graphics Design — Feed Screen</title>
<link rel="stylesheet" href="https://fonts.googleapis.com/css2?family=Roboto:wght@300;400&display=swap">
<style>
  :root {
    --stage: #8c8676;
    --screen-dark: #23231f;
    --white: #ffffff;
    --green: #74d000;
    --green-dark: #4f9400;
    --green-text: #5aa51a;
    --banner-text: #2f4a12;
    --grey-text: #6a6a6a;
    --faint-text: #c9c9c2;
    --visor: rgba(118, 116, 100, 0.78);
    --plate: rgba(70, 70, 60, 0.55);
    --stats: rgba(18, 28, 48, 0.72);
    --bar: rgba(32, 32, 28, 0.94);
  }
  * { box-sizing: border-box; margin: 0; padding: 0; }
  html, body {
    width: 1117px; height: 1200px; overflow: hidden;
    background: var(--stage);
    font-family: "Roboto", "Helvetica Neue", Arial, sans-serif;
    font-weight: 300;
  }
  .screen {
    position: absolute; left: 232px; top: 24px;
    width: 652px; height: 1152px; overflow: hidden;
    background: var(--screen-dark);
  }
  .abs { position: absolute; }
  .top-strip { left: 0; top: 0; width: 652px; height: 22px;
    background: linear-gradient(90deg, #3a2a2a, #5a3a3a 50%, #2c2c28); }
  .post-card { left: 26px; width: 600px; background: var(--white); }
  .post-card--top { top: 20px; height: 150px; }
  .banner {
    left: 26px; top: 56px; width: 590px; height: 68px;
    background: var(--green);
    display: flex; align-items: center; justify-content: center;
    font-size: 42px; color: var(--banner-text);
  }
  .banner-fold { left: 616px; top: 56px; width: 14px; height: 80px;
    background: var(--green-dark); clip-path: polygon(0 0, 100% 14%, 100% 100%, 0 86%); }
  .banner-sub { left: 26px; top: 126px; width: 600px; text-align: center;
    font-size: 18px; line-height: 22px; color: var(--faint-text); }
  .visor { left: 0; top: 166px; width: 652px; height: 156px;
    background: linear-gradient(180deg, rgba(140,138,120,0.55), var(--visor)); }
  .plate { width: 256px; height: 96px; background: var(--plate); border-radius: 6px; }
  .btn {
    width: 236px; height: 86px; border-radius: 4px;
    display: flex; align-items: center; justify-content: center; gap: 16px;
    font-size: 24px; letter-spacing: 0.5px;
  }
  .btn--promote { background: var(--green); color: var(--white); border: 2px solid #c9f28f; }
  .btn--demote { background: var(--white); color: #8a8a8a; }
  .post-photo {
    left: 0; top: 322px; width: 652px; height: 520px;
    background:
      radial-gradient(ellipse at 12% 30%, #2f7a3a 0, rgba(47,122,58,0) 45%),
      radial-gradient(ellipse at 55% 70%, #6fb6ff 0, rgba(111,182,255,0) 40%),
      linear-gradient(180deg, #1b2c4a, #2a4f8a 55%, #1a2e55);
  }
  .share { left: 562px; top: 356px; }
  .stats {
    left: 26px; top: 740px; width: 600px; height: 80px; border-radius: 6px;
    background: var(--stats); display: flex; color: var(--white);
  }
  .stat { flex: 1; display: flex; align-items: center; justify-content: center; gap: 12px;
    font-size: 20px; border-right: 1px solid rgba(255,255,255,0.2); }
  .stat:last-child { border-right: 0; }
  .stat--score { font-size: 30px; }
  .post-card--bottom { top: 842px; height: 200px; text-align: center; }
  .place-name { margin-top: 26px; font-size: 28px; line-height: 34px; color: var(--green-text); font-weight: 400; }
  .place-address { margin-top: 8px; font-size: 22px; line-height: 26px; color: var(--grey-text); }
  .tab-bar { left: 0; top: 1036px; width: 652px; height: 116px; background: var(--bar); }
  .tab-icon { top: 1060px; }
</style>
</head>
<body>
<main class="screen">
  <div class="abs top-strip"></div>
  <section class="abs post-card post-card--top"></section>
  <div class="abs banner">Love My Friends</div>
  <div class="abs banner-fold"></div>
  <p class="abs banner-sub">235 Main Street, Brookhollow, BH 10012</p>

  <div class="abs post-photo" role="img" aria-label="Photo of a blue waterfall over dark rocks with green leaves"></div>
  <svg class="abs share" width="62" height="62" viewBox="0 0 62 62" fill="none" stroke="#fff" stroke-width="2">
    <circle cx="31" cy="31" r="29"/>
    <path d="M20 40c2-9 8-13 18-13v-6l9 9-9 9v-6c-8 0-13 2-18 7z"/>
  </svg>
  <div class="abs stats">
    <div class="stat">
      <svg width="20" height="26" viewBox="0 0 20 26" fill="none" stroke="#fff" stroke-width="2"><path d="M10 25S2 15 2 9a8 8 0 0 1 16 0c0 6-8 16-8 16z"/><circle cx="10" cy="9" r="3"/></svg>
      0.01 mi
    </div>
    <div class="stat stat--score">
      <svg width="38" height="36" viewBox="0 0 38 36" fill="none" stroke="#fff" stroke-width="2"><path d="M19 2l5 11 12 1-9 8 3 12-11-6-11 6 3-12-9-8 12-1z"/></svg>
      2 930
    </div>
    <div class="stat">
      <svg width="24" height="24" viewBox="0 0 24 24" fill="none" stroke="#fff" stroke-width="2"><circle cx="12" cy="12" r="10"/><path d="M12 6v6l-4 3"/></svg>
      4 hrs ago
    </div>
  </div>

  <section class="abs post-card post-card--bottom">
    <h2 class="place-name">Verdant Falls</h2>
    <p class="place-address">1 St., Verdant Falls, VF 48215</p>
  </section>
  <div class="abs plate" style="left:40px;top:960px"></div>
  <div class="abs plate" style="left:350px;top:960px"></div>
  <div class="abs btn btn--promote" style="left:50px;top:970px">
    <svg width="32" height="30" viewBox="0 0 32 30" fill="none" stroke="#fff" stroke-width="2"><path d="M2 13h6v15H2zM8 14l6-11c3 0 4 2 3 6l-1 3h10c2 0 3 2 2 4l-3 10c-1 2-2 2-4 2H8"/></svg>
    PROMOTE
  </div>
  <div class="abs btn btn--demote" style="left:360px;top:970px">
    DEMOTE
    <svg width="32" height="30" viewBox="0 0 32 30" fill="none" stroke="#999" stroke-width="2"><path d="M30 17h-6V2h6zM24 16l-6 11c-3 0-4-2-3-6l1-3H6c-2 0-3-2-2-4l3-10c1-2 2-2 4-2h13"/></svg>
  </div>

  <div class="abs visor"></div>
  <div class="abs plate" style="left:40px;top:166px"></div>
  <div class="abs plate" style="left:350px;top:166px"></div>
  <div class="abs btn btn--promote" style="left:50px;top:176px">
    <svg width="32" height="30" viewBox="0 0 32 30" fill="none" stroke="#fff" stroke-width="2"><path d="M2 13h6v15H2zM8 14l6-11c3 0 4 2 3 6l-1 3h10c2 0 3 2 2 4l-3 10c-1 2-2 2-4 2H8"/></svg>
    PROMOTE
  </div>
  <div class="abs btn btn--demote" style="left:360px;top:176px">
    DEMOTE
    <svg width="32" height="30" viewBox="0 0 32 30" fill="none" stroke="#999" stroke-width="2"><path d="M30 17h-6V2h6zM24 16l-6 11c-3 0-4-2-3-6l1-3H6c-2 0-3-2-2-4l3-10c1-2 2-2 4-2h13"/></svg>
  </div>

  <nav class="abs tab-bar"></nav>
  <svg class="abs tab-icon" style="left:40px" width="66" height="54" viewBox="0 0 66 54" fill="none" stroke="#fff" stroke-width="3">
    <path d="M4 14h14l5-8h20l5 8h14v36H4z"/><circle cx="33" cy="30" r="11"/>
  </svg>
  <svg class="abs tab-icon" style="left:562px;top:1052px" width="50" height="66" viewBox="0 0 50 66" fill="none" stroke="#fff" stroke-width="3">
    <circle cx="25" cy="22" r="18"/>
    <path d="M25 12l3 7 7 1-5 5 1 7-6-3-6 3 1-7-5-5 7-1z" fill="#fff"/>
    <path d="M14 36L6 60l9-4 5 8 5-14M36 36l8 24-9-4-5 8-5-14"/>
  </svg>
</main>
</body>
</html>
```